Info Graphic for Luminous Stride Academy

WELCOME To The Luminous Stride Academy (LSA)

We are wanting to create a visual info graphic display of a newly designed transformational pathway program.

Please display the following heading:

The Luminous Stride Academy (LSA) Pathway Program

Subheading:

“Feeling alive and living the life you want to be living.”

Please display each step along the path clearly and with visuals representations that reflect the energy of the word and achievement accomplished.

We would like to display each step individually whilst tying to capture a flow of progression whilst maintaining the look and feel of each step.

The infographic design wants to really spark people’s attention, create impact and a curiosity resulting in a desire to seek more information regarding the program.

Energetic vibrant colours and flow are a must.

A sense of Playfulness, fun and energy is what we are looking for with this design.

The pathway is progressive with each step building on the last and I would like this to be represented in a linear fashion and NOT show steps as hierarchical.

The below documents the steps in order of progression and describes the key focus and outcome for each of the steps.

THE LSA PATHWAY:

Step 1: Intriguing You - Discover the path to transformation and igniting your relationships and life.

Step 2: Energizing You - Introduction to the Foundational principles.

Step 3: Awakening You - Creating juicy, deep connections with self and others.

Step 4: Transforming You - Feeling alive and creating a life of clarity and flow.

Step 5: Igniting You - Discovering that “This S**T Works” by living the life you want to be living.

Additional Modules available at Transforming You (by invitation)

Additional Step: Launching You - Learn to share the principles and tools to facilitate the LSA Path for family, friends and clients.

Additional Step: Aligning You - How do couples co-create a relationship that is on fire with passion and expression?

I have attached a previous style guide that we have utilised however don’t want to be limited to just this in the designs.

Happy for this to be utilised and included in designs and we are very open to do something completely different, please be creative.

Any questions or further information required, please let me know.

Target Market(s)

People looking to Feel alive and living the life you want to be living

Industry/Entity Type

Relationship and Personal Development

Requirements
Must have
• Creativity
Nice to have
• Linear display of steps and the explanations at each step included in the description
Should not have
• display hierarchy

```html
<!DOCTYPE html>
<html lang="en">
<head>
<meta charset="utf-8">
<title>Luminous Stride Academy – Pathway Program</title>
<link href="https://fonts.googleapis.com/css2?family=Oswald:wght@500&family=Montserrat:wght@400;700&display=swap" rel="stylesheet">
<style>
  :root {
    --page: #ffffff;
    --sky: #13c3fb;
    --blue: #3f8fee;
    --violet: #7a3ddf;
    --plum: #a04aa8;
    --gold: #f7a81b;
    --white: #ffffff;
    --rule: #2ad0f5;
    --head-font: "Oswald", "Arial Narrow", sans-serif;
    --body-font: "Montserrat", Arial, sans-serif;
  }
  * { box-sizing: border-box; margin: 0; padding: 0; }
  html, body {
    width: 1200px; height: 1200px; overflow: hidden;
    background: var(--page);
  }
  .poster {
    position: absolute; left: 330px; top: 0;
    width: 540px; height: 1200px;
    background: linear-gradient(180deg, var(--sky) 0%, var(--blue) 24%, var(--violet) 62%, var(--plum) 100%);
    color: var(--white);
    font-family: var(--body-font);
    overflow: hidden;
  }
  .brand {
    position: absolute; top: 62px; left: 0; width: 540px;
    display: flex; align-items: center; justify-content: center; gap: 14px;
  }
  .brand-dot { width: 46px; height: 46px; border-radius: 50%; background: var(--white); }
  .brand-name {
    font-family: var(--body-font); font-weight: 700; font-size: 19px;
    letter-spacing: 2px; color: var(--white);
  }
  .headline {
    position: absolute; top: 150px; left: 0; width: 540px;
    text-align: center; font-family: var(--head-font); font-weight: 500;
    line-height: 1.02;
  }
  .headline .line-1 { display: block; font-size: 52px; }
  .headline .line-2 { display: block; font-size: 41px; }
  .rule { position: absolute; left: 79px; width: 397px; height: 1px; background: var(--rule); }
  .rule.top { top: 252px; }
  .rule.bottom { top: 1015px; }
  .connectors { position: absolute; inset: 0; z-index: 0; }
  .step-number, .step-title {
    position: absolute; font-family: var(--head-font); font-weight: 500;
    color: var(--gold); line-height: 1; z-index: 2;
  }
  .step-number { font-size: 74px; }
  .step-title { font-size: 37px; white-space: nowrap; }
  .step-text {
    position: absolute; font-size: 14px; line-height: 17.5px; color: var(--white); z-index: 2;
  }
  .art { position: absolute; z-index: 1; }
  .art.binoculars { left: 325px; top: 258px; width: 192px; height: 135px; border-radius: 40% 50% 30% 45%;
    background: linear-gradient(135deg, #2ec3e6, #f39a86 60%, #6b4bb0); }
  .art.battery { left: 61px; top: 388px; width: 138px; height: 138px; border-radius: 50%;
    background: linear-gradient(135deg, #b04fa6, #8d3c9b); }
  .art.leaper { left: 412px; top: 505px; width: 114px; height: 118px; border-radius: 50% 50% 40% 60%;
    background: linear-gradient(160deg, #f4e11a, #f3a23f 60%, #e88b5e); }
  .art.reclining { left: 345px; top: 565px; width: 150px; height: 90px; border-radius: 30% 40% 20% 20%;
    background: linear-gradient(135deg, #f2d21c, #c53a59 50%, #e9e3f4); }
  .art.flyer { left: 50px; top: 660px; width: 180px; height: 135px; border-radius: 45% 55% 50% 40%;
    background: linear-gradient(150deg, #f7ecdc, #2d2a5a 60%, #49c49b); }
  .art.hearts { left: 338px; top: 822px; width: 182px; height: 128px; border-radius: 40%;
    background: linear-gradient(135deg, #f0444e, #e95b5b 55%, #b9e6ec); }
  .art.reacher { left: 260px; top: 960px; width: 58px; height: 205px; border-radius: 45% 45% 40% 40%;
    background: linear-gradient(180deg, #e9434f, #2e6f9a 40%, #b0865a 75%, #e9434f); }
</style>
</head>
<body>
<main class="poster">
  <header class="brand">
    <span class="brand-dot"></span>
    <span class="brand-name">Luminous Stride Academy</span>
  </header>

  <h1 class="headline">
    <span class="line-1">Feeling alive and living</span>
    <span class="line-2">the life you want to be living</span>
  </h1>
  <div class="rule top"></div>

  <svg class="connectors" width="540" height="1200" viewBox="0 0 540 1200" fill="none" stroke="rgba(255,255,255,0.7)" stroke-width="1">
    <polyline points="87,342 87,377 229,377 229,421"/>
    <polyline points="229,500 229,539 87,539 87,556"/>
    <polyline points="87,636 87,670 270,670 270,832 97,832 97,845"/>
    <circle cx="229" cy="419" r="2.5" fill="#f7a81b" stroke="none"/>
  </svg>

  <section class="step step-1">
    <span class="step-number" style="left:70px;top:276px;">1</span>
    <h2 class="step-title" style="left:109px;top:280px;">Intriguing You</h2>
    <p class="step-text" style="left:109px;top:323px;width:205px;">Discover the path to transformation and igniting your relationships and life.</p>
    <div class="art binoculars" role="img" aria-label="Illustration of a curious woman looking through binoculars among leaves"></div>
  </section>

  <section class="step step-2">
    <div class="art battery" role="img" aria-label="Illustration of an energy drink bottle and a charged battery in a purple circle"></div>
    <span class="step-number" style="left:210px;top:416px;">2</span>
    <h2 class="step-title" style="left:255px;top:420px;">Energizing You</h2>
    <p class="step-text" style="left:255px;top:462px;width:200px;">Introduction to the Foundational principles.</p>
    <div class="art leaper" role="img" aria-label="Illustration of a person leaping over a bright yellow shape"></div>
  </section>

  <section class="step step-3">
    <span class="step-number" style="left:70px;top:558px;">3</span>
    <h2 class="step-title" style="left:117px;top:562px;">Awakening You</h2>
    <p class="step-text" style="left:117px;top:603px;width:185px;">Creating juicy, deep connections with self and others.</p>
    <div class="art reclining" role="img" aria-label="Illustration of a person lying back with legs raised"></div>
  </section>

  <section class="step step-4">
    <div class="art flyer" role="img" aria-label="Illustration of a person flying freely through the air"></div>
    <span class="step-number" style="left:244px;top:689px;">4</span>
    <h2 class="step-title" style="left:287px;top:692px;">Transforming You</h2>
    <p class="step-text" style="left:291px;top:730px;width:200px;">Feeling alive and creating a life of clarity and flow.</p>
  </section>

  <section class="step step-5">
    <span class="step-number" style="left:75px;top:850px;">5</span>
    <h2 class="step-title" style="left:126px;top:853px;">Igniting You</h2>
    <p class="step-text" style="left:126px;top:896px;width:200px;">Discovering that “This S**T Works” by living the life you want to be living.</p>
    <div class="art hearts" role="img" aria-label="Illustration of two happy hearts on a seesaw"></div>
  </section>

  <div class="rule bottom"></div>
  <div class="art reacher" role="img" aria-label="Illustration of a person reaching up toward a floating heart"></div>

  <section class="step step-launch">
    <h2 class="step-title" style="left:49px;top:1044px;">Launching You</h2>
    <p class="step-text" style="left:53px;top:1090px;width:190px;">Learn to share the principles and tools to facilitate the LSA Path for family, friends and clients.</p>
  </section>

  <section class="step step-align">
    <h2 class="step-title" style="left:324px;top:1044px;">Aligning You</h2>
    <p class="step-text" style="left:328px;top:1090px;width:150px;">How do couples co-create a relationship that is on fire with passion and expression?</p>
  </section>
</main>
</body>
</html>
```